Postcard Design

I'm hosting a retreat in Tuscany tag line ideas for front: "nourish your soul with a taste of Tuscany" or "Savor the sweet life and Nourish your soul with a taste of Tuscany" here is the pertinent info- trip date: September 5-12, 2015 number:1.877.384.2951 e/m:Info@WillowmereRetreats.example Web address:www.WillowmereRetreats.example
What's included:
• 7 nights Accommodations in beautiful Villa
• All Meals and Snacks included
• Special Wine tasting Excursion in Chianti
• Guided Tour of Siena
• Hands on Cooking Class at the villa
• Yoga, Meditation walks, Journaling
Something like this should be on back lower right side: Spaces Limited Reserve Yours Today!
Other wording ideas for back: Renew your spirit in the quiet beauty of the Tuscan landscape (maybe above what's included)
This can be near the "spaces limited" =Invest in your health, spirit and well-being *airfare not included. See website for details
More ideas/maybe a better way to word all this??:
Welcome to "la dolce vita" (The sweet life)
Have you always wanted to travel to Italy? Want to experience the culture in a special way you couldn't enjoy as a typical tourist? This is the trip you've been waiting for. Life is too short to wait any longer!
Hosts show with pictures:
Lise Karen Bouchard woman w/dark hair headshot
Retreat host
Sharing her love of Italy's beautiful culture with you is her special gift
And
Greta Halvorsen
Personal wellness consultant
Yoga, Meditation, Asana, Reiki, Pilates

I included a photo of the current postcard I made front & back. You can also visit my website to get an idea of my style. I'm hoping you can make me a postcard that's more tantalizing, and will get me some clients! I will include some extra photos and feel free to use your own stock images... anything to help! Feel free to change up wording to make it more appealing, welcoming and make people chose to go on retreat with me instead the hundreds of other retreats out there.
Thank you
Lise Karen

```html
<!DOCTYPE html>
<html lang="en">
<head>
<meta charset="utf-8">
<title>Willowmere Retreats – Tuscany Postcard</title>
<link rel="stylesheet" href="https://fonts.googleapis.com/css2?family=Berkshire+Swash&family=Fredoka:wght@600&family=Kaushan+Script&family=Montserrat:wght@600;700&family=Tinos:wght@400;700&display=swap">
<style>
  :root {
    --backdrop: #e9e4da;
    --olive: #8c9460;
    --sun-yellow: #f5d31c;
    --brick: #b2432a;
    --ink: #1f1a14;
    --paper: #f4efe4;
    --weathered: #cfcac2;
    --weathered-dark: #b8b3aa;
    --white: #ffffff;
  }
  * { margin: 0; padding: 0; box-sizing: border-box; }
  html, body { width: 1200px; height: 450px; overflow: hidden; }
  body { background: var(--backdrop); position: relative; font-family: "Tinos", serif; }

  .card { position: absolute; top: 32px; width: 533px; height: 383px; overflow: hidden; box-shadow: 0 2px 6px rgba(0,0,0,.25); }
  .card--front { left: 55px; background: var(--paper); }
  .card--back { left: 614px; background: linear-gradient(90deg, var(--weathered) 0%, var(--weathered-dark) 50%, var(--weathered) 100%); }

  .photo { position: absolute; }

  /* front */
  .front-header { left: 0; top: 0; width: 533px; height: 90px;
    background: linear-gradient(180deg, #b9c6b4 0%, #96a56a 55%, #7e8a3e 100%); }
  .brand { position: absolute; left: 0; width: 533px; text-align: center; top: 14px; }
  .brand__name { font-family: "Tinos", serif; font-weight: 700; color: var(--ink); font-size: 34px; line-height: 1; }
  .brand__sub { font-family: "Tinos", serif; font-weight: 700; color: var(--ink); font-size: 17px; letter-spacing: 5px; margin-top: 4px; }
  .front-band { position: absolute; left: 0; top: 90px; width: 533px; height: 38px; background: var(--olive);
    font-family: "Fredoka", sans-serif; font-weight: 600; color: var(--sun-yellow); font-size: 23px;
    text-align: center; line-height: 38px; letter-spacing: .5px; }
  .front-villa { left: 0; top: 128px; width: 533px; height: 255px;
    background: linear-gradient(180deg, #dbe6ef 0%, #c7d8e6 14%, #6d8b3c 30%, #b89a55 52%, #7fa245 72%, #5f8a32 100%); }
  .trip-date { position: absolute; top: 132px; left: 0; width: 533px; text-align: center;
    font-family: "Tinos", serif; font-weight: 700; font-size: 20px; color: var(--ink); }
  .front-tagline { position: absolute; right: 14px; top: 212px; width: 235px; text-align: right;
    font-family: "Kaushan Script", cursive; color: var(--white); font-size: 19px; line-height: 1.25;
    text-shadow: 0 1px 3px rgba(0,0,0,.55); }

  /* back */
  .back-village { left: 12px; top: 10px; width: 124px; height: 180px;
    background: linear-gradient(180deg, #8fb2d4 0%, #a88565 35%, #8c6a4e 70%, #6b5a48 100%); }
  .back-tower { left: 12px; top: 196px; width: 124px; height: 176px;
    background: linear-gradient(180deg, #c7d6e3 0%, #9a5a3e 35%, #7c6a4a 70%, #5f7a4a 100%); }
  .back-headline { position: absolute; left: 143px; top: 5px; width: 390px; height: 52px;
    background: rgba(244,239,228,.85); padding: 2px 8px;
    font-family: "Berkshire Swash", cursive; color: var(--brick); font-size: 19px; line-height: 1.22; font-weight: 400; }
  .itinerary { position: absolute; left: 143px; top: 57px; width: 197px; height: 315px;
    background: var(--olive); color: var(--white); padding: 6px 5px 0 6px;
    font-size: 11.6px; line-height: 12.6px; white-space: nowrap; }
  .itinerary__intro { margin-bottom: 3px; }
  .itinerary__list { list-style: none; }
  .itinerary__list li { position: relative; padding-left: 10px; }
  .itinerary__list li::before { content: ""; position: absolute; left: 1px; top: 4px; width: 5px; height: 5px; border-radius: 50%; background: var(--sun-yellow); }
  .itinerary__invest { color: var(--sun-yellow); font-weight: 700; text-align: center; margin: 6px 0 6px; }
  .itinerary__reserve { color: var(--sun-yellow); font-weight: 700; margin-top: 2px; }
  .itinerary__note { margin-top: 6px; }
  .contact { margin-top: 6px; margin-left: 6px; font-family: "Montserrat", sans-serif; font-weight: 700; font-size: 9.4px; line-height: 14px; }
  .contact svg { vertical-align: -1px; margin-right: 3px; }
  .back-hills { left: 371px; top: 53px; width: 152px; height: 143px;
    background: linear-gradient(180deg, #9fb7c9 0%, #b8c27e 30%, #7d9a3c 65%, #5c7a2e 100%); }
  .love-affair { position: absolute; left: 352px; top: 192px; width: 180px; text-align: center;
    font-weight: 700; font-size: 12px; line-height: 12.8px; color: var(--ink); }
  .love-affair__dates { color: var(--brick); display: block; margin-top: 1px; }
  .back-brand { position: absolute; left: 352px; top: 310px; width: 180px; text-align: center; }
  .back-brand .brand__name { color: var(--brick); font-size: 24px; }
  .back-brand .brand__sub { color: var(--brick); font-size: 12px; letter-spacing: 4px; margin-top: 3px; }
</style>
</head>
<body>
  <section class="card card--front">
    <div class="photo front-header" role="img" aria-label="Tuscan hills with sunflowers in the corners"></div>
    <div class="brand">
      <div class="brand__name">Willowmere</div>
      <div class="brand__sub">RETREATS</div>
    </div>
    <div class="front-band">THE TRIP OF A LIFETIME ~ TUSCANY 2015</div>
    <div class="photo front-villa" role="img" aria-label="Tuscan villa with pool among cypress trees and golden fields"></div>
    <p class="trip-date">Trip Date: September 5-12, 2015</p>
    <p class="front-tagline">Savor the sweet life<br>and Nourish your soul<br>with a taste of Tuscany</p>
  </section>

  <section class="card card--back">
    <div class="photo back-village" role="img" aria-label="Stone village lane with steps"></div>
    <div class="photo back-tower" role="img" aria-label="Ivy covered medieval tower above green hills"></div>
    <h2 class="back-headline">Renew Your Spirit in the quiet<br>beauty of the Tuscan landscape</h2>
    <div class="itinerary">
      <p class="itinerary__intro">Nourishing Retreat for Your Body &amp;<br>Soul ~ our exciting itinerary includes:</p>
      <ul class="itinerary__list">
        <li>7 nights Accommodations in<br>beautiful Villa</li>
        <li>All Meals and Snacks included</li>
        <li>Special Wine tasting Excursion<br>in Chianti</li>
        <li>Guided Tour of Siena</li>
        <li>Hands on Cooking Class at the villa</li>
        <li>Yoga, Meditation walks, Journaling</li>
      </ul>
      <p class="itinerary__invest">Invest in your health,<br>spirit and well-being</p>
      <p>We have an overwhelming amount of<br>requests to join us this Fall. Spaces will<br>be allotted “first come, first served”.</p>
      <p class="itinerary__reserve">Reserve Yours Today!</p>
      <p class="itinerary__note">*Airfare not included.<br>See website for details</p>
      <div class="contact">
        <div>www.WillowmereRetreats.example</div>
        <div><svg width="10" height="10" viewBox="0 0 10 10" aria-hidden="true"><circle cx="5" cy="5" r="4.4" fill="none" stroke="#fff" stroke-width="1"/><path d="M3.4 2.8c.3 1.9 1.5 3.3 3.2 4l.6-.9-1-.6-.5.5c-.6-.4-1-.9-1.3-1.5l.5-.5-.6-1z" fill="#fff"/></svg>1.877.384.2951</div>
        <div>Info@WillowmereRetreats.example</div>
      </div>
    </div>
    <div class="photo back-hills" role="img" aria-label="Rolling green Tuscan hills with a farmhouse and sunflowers"></div>
    <p class="love-affair">Come have a love affair<br>with Italy and the<br>beguiling beauty<br>of Tuscany.<br>Savor the sweet life ~<br>living la dolce vita.<span class="love-affair__dates">September 5th<br>to 12th 2015</span></p>
    <div class="back-brand">
      <div class="brand__name">Willowmere</div>
      <div class="brand__sub">RETREATS</div>
    </div>
  </section>
</body>
</html>
```